Conference Oversize Name Badge

Design an oversized name badge that would be worn by conference attendees using a lanyard.

Things to include on the name badge
- attendee's headshot (photo)
- attendee's first name and last name
- attendee's company name
- conference organizer company name
- conference organizer logo (attached)
- barcode
- attendee type color theme. For example: sponsor would have a red color theme, exhibitor would have blue color theme. Same badges but with different color themes.

Get creative!

Please let me know if you have any questions.

Industry/Entity Type

Event Planning

Requirements
Must have
• Whats important:
• 1. Attendee name and company name needs to be big and prominent and easily readable.
• 2. Incorporate attached conference organizer logo
• 3. Be creative
Should not have
• Please do not submit boring rectangle name badges.

```html
<!DOCTYPE html>
<html lang="en">
<head>
<meta charset="utf-8">
<title>Sponsor Badge – Talia Whitmore</title>
<link rel="stylesheet" href="https://fonts.googleapis.com/css2?family=Fredoka:wght@500;600&family=Open+Sans:wght@700&display=swap">
<style>
  :root {
    --theme-red: #e8605e;
    --theme-red-deep: #d8434a;
    --theme-red-warm: #f07a5a;
    --panel: #f8f1f1;
    --ink-dark: #3a3431;
    --ink-mid: #675d55;
    --ink-soft: #9d8f80;
    --org-ink: #6a6d78;
    --org-mark: #3f86a6;
    --photo-top: #d9d7d9;
    --photo-bottom: #b9a89c;
  }
  html, body { margin: 0; padding: 0; overflow: hidden; background: #ffffff; }
  .badge {
    position: relative;
    width: 900px; height: 1200px;
    overflow: hidden;
  }
  .badge__texture {
    position: absolute; inset: 0;
    background:
      radial-gradient(circle at 30% 40%, var(--theme-red-warm) 0%, transparent 45%),
      radial-gradient(circle at 80% 85%, var(--theme-red-deep) 0%, transparent 50%),
      linear-gradient(160deg, var(--theme-red) 0%, var(--theme-red-deep) 100%);
  }
  .badge__panel { position: absolute; inset: 0; }
  .attendee-type {
    position: absolute; left: 20px; top: 58px; width: 150px; margin: 0;
    display: flex; flex-direction: column; align-items: center;
    font-family: "Fredoka", sans-serif; font-weight: 600;
    font-size: 200px; line-height: 153px; color: var(--ink-dark);
    text-shadow: 3px 3px 4px rgba(40, 110, 120, 0.6);
  }
  .organizer {
    position: absolute; left: 220px; top: 145px;
    display: flex; align-items: center; gap: 26px;
  }
  .organizer__mark {
    width: 130px; height: 130px; border-radius: 50%;
    background: var(--org-mark);
  }
  .organizer__name {
    margin: 0; font-family: "Open Sans", sans-serif; font-weight: 700;
    font-size: 30px; color: var(--org-ink);
  }
  .headshot {
    position: absolute; left: 402px; top: 260px; width: 275px; height: 337px;
    border: 3px solid #111;
    background: linear-gradient(180deg, var(--photo-top) 0%, var(--photo-bottom) 100%);
  }
  .attendee {
    position: absolute; left: 175px; right: 0; top: 610px; margin: 0;
    text-align: center; font-family: "Fredoka", sans-serif; font-weight: 600;
  }
  .attendee__first { display: block; font-size: 200px; line-height: 190px; color: var(--ink-dark); padding-left: 30px; }
  .attendee__last { display: block; font-size: 98px; line-height: 100px; color: var(--ink-mid); padding-left: 20px; }
  .attendee__company {
    position: absolute; left: 175px; right: 0; top: 912px; margin: 0;
    text-align: center; font-family: "Fredoka", sans-serif; font-weight: 500;
    font-size: 43px; color: var(--ink-soft); padding-left: 10px;
  }
</style>
</head>
<body>
<main class="badge">
  <div class="badge__texture" role="img" aria-label="Painted red and coral texture with faint greetings in several languages"></div>

  <svg class="badge__panel" width="900" height="1200" viewBox="0 0 900 1200" aria-hidden="true">
    <polygon fill="var(--panel)" points="182,178 250,150 300,118 420,92 520,150 640,92 740,130 900,95 900,1075 780,1045 640,1075 500,1040 355,1070 235,1052 188,1078 218,1000 180,930 216,850 178,760 216,680 180,605 216,520 178,440 216,350 180,265 216,205"/>
  </svg>

  <h2 class="attendee-type" aria-label="Sponser">
    <span>S</span><span>p</span><span>o</span><span>n</span><span>s</span><span>e</span><span>r</span>
  </h2>

  <header class="organizer">
    <span class="organizer__mark" aria-hidden="true"></span>
    <p class="organizer__name">Northgate Events LLC</p>
  </header>

  <div class="headshot" role="img" aria-label="Attendee headshot photo"></div>

  <h1 class="attendee">
    <span class="attendee__first">Talia</span>
    <span class="attendee__last">Whitmore</span>
  </h1>
  <p class="attendee__company">Harlow &amp; Sons Life Insurance</p>
</main>
</body>
</html>
```